Harbor Crest PEO - Web Build for Professional Employment Organization

We need a website built for our new PEO (professional employment organization). This company will offer third party Human Resource services to companies who are looking to outsource:<br/>Recruiting<br/>Administrative Onboarding<br/>New hire training, ongoing training and development<br/>Payroll/compensation processing/services<br/>Employee Relations<br/>Unemployment Claim Facilitation<br/>Benefits Plans and Administration<br/><br/>I have attached the logo below. Please use that as a reference and color match as best as possible. <br/><br/>Here are some of the competitor's websites:<br/>https://www.velmorix.example/ <br/>https://www.quandrel.example/<br/>https://www.quandrel.example/<br/>https://www.tzv.example/<br/>https://www.brindaxo.example/<br/>https://lumbrasto.example/contact-lumbra/<br/><br/>

Target Market(s)

Startups and mid-sized businesses

Number of Pages Required

5+ page

Font styles to use
Sans Serif

Colors
0592cd

Requirements
Must have
• Features Pages
• SEO driven keyword rich content
• Strong focus on our ability to provide unemployment claim facilitation services as well as mandatory training/certification fulfillment
Nice to have
• I'd like to see one mockup with a Live Chat version if possible. In theory, the Live Chat messages would go directly to our front desk person.

```html
<!DOCTYPE html>
<html lang="en">
<head>
<meta charset="utf-8">
<title>Harbor Crest PEO</title>
<link href="https://fonts.googleapis.com/css2?family=Nunito:wght@400;600;700;800;900&display=swap" rel="stylesheet">
<style>
:root{
  --teal:#1d9ab2;
  --teal-dark:#16879c;
  --navy:#2c3852;
  --ink:#4a5161;
  --muted:#7b8190;
  --light:#eef0f3;
  --footer:#1e2332;
  --white:#ffffff;
}
*{margin:0;padding:0;box-sizing:border-box}
html,body{width:1200px;height:4468px;overflow:hidden}
body{position:relative;font-family:"Nunito",sans-serif;color:var(--ink);background:var(--white)}
.abs{position:absolute}
p{font-size:13px;line-height:1.65}

/* header */
.site-header{left:0;top:0;width:1200px;height:80px;background:var(--white)}
.brand{left:40px;top:22px;font-size:26px;font-weight:900;color:var(--navy);letter-spacing:1px;line-height:1}
.brand small{display:block;font-size:13px;letter-spacing:6px;text-align:center;margin-top:3px}
.main-nav{left:540px;top:33px;display:flex;gap:26px;font-size:11px;font-weight:700;color:var(--navy);white-space:nowrap}
.main-nav .active{color:var(--teal);border-bottom:2px solid var(--teal);padding-bottom:4px}
.search-btn{left:936px;top:24px;width:32px;height:32px;border:2px solid var(--navy);border-radius:50%}
.search-btn svg{position:absolute;left:6px;top:6px}
.btn-login{left:984px;top:26px;width:70px;height:28px;border-radius:14px;background:var(--teal);color:var(--white);font-size:11px;font-weight:800;text-align:center;line-height:28px}
.btn-support{left:1070px;top:26px;width:84px;height:28px;border-radius:14px;border:2px solid var(--navy);color:var(--navy);font-size:11px;font-weight:800;text-align:center;line-height:24px}

/* hero */
.hero{left:0;top:80px;width:1200px;height:620px}
.hero-title{left:40px;top:104px;color:var(--white);font-weight:900;line-height:1}
.hero-title .l1{font-size:58px;display:block}
.hero-title .l2{font-size:54px;display:block;color:#7fd3e3;margin-top:6px}
.hero-title .l3{font-size:28px;display:block;font-weight:700;margin-top:14px;line-height:1.3}
.btn-pill{height:46px;border-radius:23px;font-size:13px;font-weight:800;line-height:46px;text-align:center}
.btn-quote{left:160px;top:476px;width:270px;background:var(--white);color:var(--teal)}
.btn-demo{left:452px;top:476px;width:268px;border:2px solid var(--white);color:var(--white);line-height:42px}

/* section headings */
.section-mark{width:28px;height:28px;border:3px solid var(--teal);border-radius:50%}
.section-title{font-size:38px;font-weight:800;color:var(--navy);text-align:center;width:1200px;left:0}
.title-rule{width:60px;height:3px;background:var(--teal);left:570px}

/* about */
.about-deco{left:0;top:760px;width:260px;height:520px}
.about-photo{left:100px;top:774px}
.about-mark{left:592px;top:834px}
.about-title{left:592px;top:872px;font-size:38px;font-weight:800;color:var(--navy)}
.about-text{left:592px;top:940px;width:560px;color:var(--muted)}
.about-text p+p{margin-top:10px}
.btn-small{height:30px;border-radius:15px;background:var(--teal);color:var(--white);font-size:11px;font-weight:800;line-height:30px;padding:0 16px}
.about-more{left:592px;top:1146px}

/* services */
.services{left:0;top:1300px;width:1200px;height:1140px;background:var(--light)}
.service-card{width:282px;height:340px}
.service-card.raised{background:var(--white);box-shadow:0 12px 30px rgba(30,40,60,.14)}
.service-photo{position:absolute;left:0;top:0;width:282px;height:168px}
.service-card h3{position:absolute;left:12px;top:184px;width:260px;font-size:15px;font-weight:800;color:var(--teal);line-height:1.25}
.service-card p{position:absolute;left:12px;top:232px;width:258px;font-size:12px;color:var(--muted)}
.read-pill{position:absolute;right:12px;top:306px;height:22px;padding:0 12px;border-radius:11px;background:#d9dce2;font-size:10px;font-weight:700;color:var(--navy);line-height:22px}
.raised .read-pill{background:var(--teal);color:var(--white)}
.dots{left:560px;top:2370px;display:flex;gap:14px}
.dots span{width:12px;height:12px;border-radius:50%;background:#b9bec8}
.dots span.on{background:var(--teal)}

/* cta */
.cta{left:0;top:2460px;width:1200px;height:480px}
.cta-text{left:0;top:2600px;width:1200px;text-align:center;color:var(--white);font-size:42px;font-weight:900;line-height:1.2}
.btn-contact{left:488px;top:2776px;width:224px;height:50px;border-radius:25px;background:var(--teal);color:var(--white);font-size:15px;font-weight:800;line-height:50px;text-align:center}

/* testimonials */
.testi-text{left:144px;top:3168px;width:540px;color:var(--muted)}
.client{left:144px;top:3350px;display:flex;align-items:center;gap:14px}
.avatar{width:46px;height:46px;border-radius:50%;background:linear-gradient(135deg,#6b7586,#c9ced6)}
.client-name{font-size:15px;font-weight:700;color:var(--navy)}
.client-role{font-size:11px;font-weight:700;color:var(--teal);letter-spacing:.5px}
.avatar-sm{width:40px;height:40px;border-radius:50%;background:linear-gradient(135deg,#7a8393,#d3d7de)}
.testi-photo{left:732px;top:3156px}

/* blog */
.blog-card{width:268px;height:370px;background:var(--white);box-shadow:0 10px 26px rgba(30,40,60,.13)}
.blog-photo{position:absolute;left:0;top:0;width:268px;height:176px}
.blog-date{position:absolute;left:14px;top:150px;width:66px;height:66px;border-radius:50%;background:var(--teal);border:4px solid var(--white);color:var(--white);text-align:center}
.blog-date b{display:block;font-size:22px;font-weight:900;line-height:1;margin-top:12px}
.blog-date span{font-size:9px;font-weight:700}
.blog-card h4{position:absolute;left:16px;top:228px;width:236px;font-size:13px;font-weight:800;color:var(--navy);line-height:1.35}
.blog-card p{position:absolute;left:16px;top:270px;width:236px;font-size:11px;color:var(--muted)}
.blog-more{position:absolute;left:16px;top:330px;font-size:12px;font-weight:800;color:var(--teal)}

/* footer */
.site-footer{left:0;top:4120px;width:1200px;height:348px;background:var(--footer);color:#c3c8d3}
.footer-brand{left:144px;top:4168px;font-size:28px;font-weight:900;color:var(--white);letter-spacing:1px;line-height:1}
.footer-brand small{display:block;font-size:14px;letter-spacing:7px;text-align:center;margin-top:3px}
.footer-about{left:144px;top:4236px;width:360px;font-size:11px;color:#aeb3bf}
.footer-head{font-size:20px;font-weight:800;color:var(--white);letter-spacing:.5px}
.footer-links{left:616px;top:4224px;list-style:none;font-size:11px;font-weight:600;line-height:26px;color:#c3c8d3}
.footer-links li::before{content:"";display:inline-block;width:5px;height:5px;border-radius:50%;background:var(--teal);margin-right:10px;vertical-align:middle}
.footer-contact{left:880px;top:4224px;font-size:11px;line-height:1.5;color:#c3c8d3}
.contact-row{display:flex;align-items:center;gap:14px;margin-bottom:16px}
.contact-ico{width:22px;height:22px;border-radius:50%;background:var(--teal);position:relative;flex:none}
.contact-ico svg{position:absolute;left:5px;top:5px}
.footer-rule{left:144px;top:4416px;width:912px;height:1px;background:#343a4b}
.copyright{left:0;top:4436px;width:1200px;text-align:center;font-size:10px;color:#8d93a0}
</style>
</head>
<body>

<!-- header -->
<header class="abs site-header">
  <div class="abs brand">HARBOR CREST<small>PEO</small></div>
  <nav class="abs main-nav"><span class="active">Home</span><span>About Us</span><span>Who We Serve</span><span>Resources</span><span>Contact</span></nav>
  <div class="abs search-btn"><svg width="16" height="16" viewBox="0 0 16 16"><circle cx="6.5" cy="6.5" r="4.5" fill="none" stroke="#2c3852" stroke-width="2"/><line x1="10" y1="10" x2="14" y2="14" stroke="#2c3852" stroke-width="2"/></svg></div>
  <div class="abs btn-login">LOG IN</div>
  <div class="abs btn-support">SUPPORT</div>
</header>

<!-- hero -->
<section class="abs hero">
  <svg width="1200" height="620" viewBox="0 0 1200 620">
    <defs>
      <linearGradient id="heroPhoto" x1="0" y1="0" x2="1" y2="1">
        <stop offset="0" stop-color="#4b5a70"/><stop offset=".55" stop-color="#8a97a8"/><stop offset="1" stop-color="#c9b8a6"/>
      </linearGradient>
    </defs>
    <rect width="1200" height="620" fill="url(#heroPhoto)" role="img" aria-label="Team of business people reviewing payroll on a laptop in a bright office"/>
    <polygon points="0,0 660,0 560,620 0,620" fill="#34415a" opacity=".9"/>
    <polygon points="1200,430 1200,620 660,620" fill="#ffffff"/>
    <line x1="1200" y1="410" x2="700" y2="600" stroke="#1d9ab2" stroke-width="6"/>
  </svg>
</section>
<h1 class="abs hero-title"><span class="l1">SIMPLIFY</span><span class="l2">HR AND PAYROLL</span><span class="l3">WITH SOFTWARE AND SERVICES<br>DESIGNED FOR YOUR BUSINESS</span></h1>
<div class="abs btn-pill btn-quote">GET A FREE QUOTE &nbsp;→</div>
<div class="abs btn-pill btn-demo">SCHEDULE A DEMO &nbsp;→</div>

<!-- about -->
<div class="abs about-deco" role="img" aria-label="Faint grey decorative backdrop" style="background:radial-gradient(circle at 20% 50%,#eceef1 0,#f6f7f8 55%,rgba(255,255,255,0) 70%)"></div>
<svg class="abs about-photo" width="460" height="460" viewBox="0 0 460 460">
  <defs><linearGradient id="aboutPhoto" x1="0" y1="0" x2="1" y2="1"><stop offset="0" stop-color="#d9dde2"/><stop offset=".5" stop-color="#b8a796"/><stop offset="1" stop-color="#7d8898"/></linearGradient></defs>
  <circle cx="230" cy="230" r="220" fill="url(#aboutPhoto)" role="img" aria-label="Woman working on paperwork and a laptop at her desk"/>
  <path d="M230 10 A220 220 0 0 1 450 230" fill="none" stroke="#1d9ab2" stroke-width="8"/>
</svg>
<div class="abs section-mark about-mark"></div>
<h2 class="abs about-title">ABOUT US</h2>
<div class="abs about-text">
  <p>Lorem ipsum dolor sit amet, consectetur adipiscing elit, sed do eiusmod tempor incididunt ut labore et dolore magna aliqua. Ut enim ad minim veniam, quis nostrud exercitation ullamco laboris nisi ut aliquip ex ea commodo consequat. Duis aute irure dolor in reprehenderit in voluptate velit esse cillum dolore eu fugiat nulla pariatur. Excepteur sint occaecat cupidatat non proident, sunt in culpa qui officia deserunt mollit anim id est laborum.</p>
  <p>Lorem ipsum dolor sit amet, consectetur adipiscing elit, sed do eiusmod tempor incididunt ut labore et dolore magna aliqua consectetur adipiscing elit, sed do eiusmod tempor.</p>
</div>
<div class="abs btn-small about-more">READ MORE &nbsp;→</div>

<!-- services -->
<section class="abs services"></section>
<div class="abs section-mark" style="left:586px;top:1400px"></div>
<h2 class="abs section-title" style="top:1436px">HARBOR CREST PEO SERVICE</h2>
<div class="abs title-rule" style="top:1494px"></div>

<div class="abs service-card" style="left:144px;top:1552px">
  <div class="service-photo" role="img" aria-label="Office shelves with files and binders" style="background:linear-gradient(135deg,#8f7a66,#c9c2b8)"></div>
  <h3>Administrative Onboarding</h3>
  <p>Lorem ipsum dolor sit amet, consectetur adipiscing elit, sed do eiusmod tempor incididunt ut labore et.</p>
  <span class="read-pill">Read More →</span>
</div>
<div class="abs service-card raised" style="left:460px;top:1552px">
  <div class="service-photo" role="img" aria-label="Businessman in a suit at a training session" style="background:linear-gradient(135deg,#5b6678,#b7bec9)"></div>
  <h3>New hire training, ongoing training and development</h3>
  <p>Lorem ipsum dolor sit amet, consectetur adipiscing elit, sed do eiusmod tempor incididunt ut labore et.</p>
  <span class="read-pill">Read More →</span>
</div>
<div class="abs service-card" style="left:768px;top:1552px">
  <div class="service-photo" role="img" aria-label="Calculator and payroll paperwork" style="background:linear-gradient(135deg,#b9a48d,#6e7a8a)"></div>
  <h3>Payroll/compensation processing/services</h3>
  <p>Lorem ipsum dolor sit amet, consectetur adipiscing elit, sed do eiusmod tempor incididunt ut labore et.</p>
  <span class="read-pill">Read More →</span>
</div>
<div class="abs service-card" style="left:144px;top:1960px">
  <div class="service-photo" role="img" aria-label="Recruiter interviewing a candidate" style="background:linear-gradient(135deg,#a38670,#e0d4c6)"></div>
  <h3>Recruiting</h3>
  <p>Lorem ipsum dolor sit amet, consectetur adipiscing elit, sed do eiusmod tempor incididunt ut labore et.</p>
  <span class="read-pill">Read More →</span>
</div>
<div class="abs service-card" style="left:460px;top:1960px">
  <div class="service-photo" role="img" aria-label="Two colleagues shaking hands" style="background:linear-gradient(135deg,#6f7c8d,#c8cdd4)"></div>
  <h3>Employee Relations</h3>
  <p>Lorem ipsum dolor sit amet, consectetur adipiscing elit, sed do eiusmod tempor incididunt ut labore et.</p>
  <span class="read-pill">Read More →</span>
</div>
<div class="abs service-card" style="left:768px;top:1960px">
  <div class="service-photo" role="img" aria-label="Woman reviewing a claim at her desk" style="background:linear-gradient(135deg,#3e4658,#a3a9b5)"></div>
  <h3>Unemployment Claim Facilitation</h3>
  <p>Lorem ipsum dolor sit amet, consectetur adipiscing elit, sed do eiusmod tempor incididunt ut labore et.</p>
  <span class="read-pill">Read More →</span>
</div>
<div class="abs dots"><span></span><span class="on"></span><span></span></div>

<!-- cta -->
<section class="abs cta" role="img" aria-label="Team meeting in a modern office, darkened" style="background:linear-gradient(90deg,#2a303c,#4d5562 45%,#3a414e)"></section>
<div class="abs cta-text">LOREM IPSUM DOLOR SIT AMET,<br>CONSECTETUR ADIPISCING ELIT, SED DO<br>EIUSMOD TEMPOR</div>
<div class="abs btn-contact">CONTACT US &nbsp;→</div>

<!-- testimonials -->
<div class="abs section-mark" style="left:586px;top:3030px"></div>
<h2 class="abs section-title" style="top:3066px">OUR TESTIMONIALS</h2>
<div class="abs title-rule" style="top:3124px"></div>
<div class="abs testi-text"><p>Lorem ipsum dolor sit amet, consectetur adipiscing elit, sed do eiusmod tempor incididunt ut labore et dolore magna aliqua. Ut enim ad minim veniam, quis nostrud exercitation ullamco laboris nisi ut aliquip ex ea commodo consequat. Duis aute irure dolor in reprehenderit in voluptate velit esse cillum dolore eu fugiat nulla pariatur. Excepteur sint occaecat cupidatat non proident, sunt in culpa qui officia deserunt mollit anim id est laborum.</p></div>
<div class="abs client">
  <div class="avatar" role="img" aria-label="Client portrait"></div>
  <div><div class="client-name">Client's Name</div><div class="client-role">DESIGNATION</div></div>
  <div class="avatar-sm" style="margin-left:60px" role="img" aria-label="Client portrait"></div>
  <div class="avatar-sm" style="margin-left:30px" role="img" aria-label="Client portrait"></div>
  <span style="color:var(--teal);font-weight:800;margin-left:10px">← &nbsp;→</span>
</div>
<svg class="abs testi-photo" width="320" height="320" viewBox="0 0 320 320">
  <defs><linearGradient id="testiPhoto" x1="0" y1="0" x2="0" y2="1"><stop offset="0" stop-color="#e3e5e8"/><stop offset="1" stop-color="#6d7789"/></linearGradient></defs>
  <circle cx="160" cy="160" r="156" fill="url(#testiPhoto)" role="img" aria-label="Portrait of a smiling businessman in a suit"/>
  <circle cx="54" cy="36" r="32" fill="#1d9ab2"/>
  <text x="54" y="56" text-anchor="middle" font-family="Nunito, sans-serif" font-size="48" font-weight="900" fill="#fff">“</text>
</svg>

<!-- blog -->
<div class="abs section-mark" style="left:586px;top:3536px"></div>
<h2 class="abs section-title" style="top:3572px">OUR BLOG</h2>
<div class="abs title-rule" style="top:3630px"></div>

<article class="abs blog-card" style="left:144px;top:3672px">
  <div class="blog-photo" role="img" aria-label="People talking at an office table" style="background:linear-gradient(135deg,#8a6f62,#d7cdc4)"></div>
  <div class="blog-date"><b>27</b><span>JAN</span></div>
  <h4>Lorem ipsum dolor sit amet, consectetur adipiscing</h4>
  <p>Lorem ipsum dolor sit amet, consectetur adipiscing elit, sed do eiusmod tempor.</p>
  <span class="blog-more">Read More &nbsp;→</span>
</article>
<article class="abs blog-card" style="left:460px;top:3672px">
  <div class="blog-photo" role="img" aria-label="Colleagues collaborating at a desk" style="background:linear-gradient(135deg,#5f6b7c,#c2c8d0)"></div>
  <div class="blog-date"><b>27</b><span>JAN</span></div>
  <h4>Lorem ipsum dolor sit amet, consectetur adipiscing</h4>
  <p>Lorem ipsum dolor sit amet, consectetur adipiscing elit, sed do eiusmod tempor.</p>
  <span class="blog-more">Read More &nbsp;→</span>
</article>
<article class="abs blog-card" style="left:776px;top:3672px">
  <div class="blog-photo" role="img" aria-label="Team meeting in a bright room" style="background:linear-gradient(135deg,#b29a84,#7e8898)"></div>
  <div class="blog-date"><b>27</b><span>JAN</span></div>
  <h4>Lorem ipsum dolor sit amet, consectetur adipiscing</h4>
  <p>Lorem ipsum dolor sit amet, consectetur adipiscing elit, sed do eiusmod tempor.</p>
  <span class="blog-more">Read More &nbsp;→</span>
</article>

<!-- footer -->
<footer class="abs site-footer"></footer>
<div class="abs footer-brand">HARBOR CREST<small>PEO</small></div>
<p class="abs footer-about">Lorem ipsum dolor sit amet, consectetur adipiscing elit, sed do eiusmod tempor incididunt ut labore et dolore magna aliqua. Ut enim ad minim veniam, quis nostrud exercitation ullamco laboris nisi ut aliquip.</p>
<div class="abs footer-head" style="left:616px;top:4168px">QUICK LINKS</div>
<ul class="abs footer-links"><li>HOME</li><li>ABOUT US</li><li>WHO WE SERVE</li><li>RESOURCES</li><li>CONTACT</li></ul>
<div class="abs footer-head" style="left:880px;top:4168px">CONTACT US</div>
<div class="abs footer-contact">
  <div class="contact-row"><span class="contact-ico"><svg width="12" height="12" viewBox="0 0 12 12"><path d="M6 1a3.5 3.5 0 0 0-3.5 3.5C2.5 7 6 11 6 11s3.5-4 3.5-6.5A3.5 3.5 0 0 0 6 1z" fill="#fff"/></svg></span><span>Lorem Ipsum Street,<br>City Name</span></div>
  <div class="contact-row"><span class="contact-ico"><svg width="12" height="12" viewBox="0 0 12 12"><path d="M2 1h2.5l1 3-1.5 1a7 7 0 0 0 3 3l1-1.5 3 1V10a1 1 0 0 1-1 1A9 9 0 0 1 1 2a1 1 0 0 1 1-1z" fill="#fff"/></svg></span><span>(555) 014 - 2290</span></div>
  <div class="contact-row"><span class="contact-ico"><svg width="12" height="12" viewBox="0 0 12 12"><rect x="1" y="2.5" width="10" height="7" fill="none" stroke="#fff" stroke-width="1.3"/><path d="M1 3l5 4 5-4" fill="none" stroke="#fff" stroke-width="1.3"/></svg></span><span>info@harborcrest.example</span></div>
</div>
<div class="abs footer-rule"></div>
<div class="abs copyright">Copyright © HARBOR CREST PEO. All rights reserved.</div>

</body>
</html>
```